Email footer for a cafe

The task is to design an email footer for a new start up cafe business. The logo has been designed, but we would like a professional email footer to sign off on all emails.

The email footer should :
1. look professional and competent
2. be clean and easy to read
3. the email must have the ability to optimise / adjust across the bottom of the email depending on the device being used to read the email
4. the design may stretch across the entire bottom of the email, but this is not mandatory
5. it must incorporate the logo and the details as listed below.
6. For any additional lines / dividers that a designer might choose to incorporate into the email footer, our preference is to match the colour of the logo.

The logo is attached. The logo details are:

The CMYK for the logo is C0 M50 Y100 K0 in font BankGothic Lt BT - Light
The CMKY for the text is C75 M68 Y67 K89 in font AvantGarde Bk BT - Book

The details to be included in the email footer are:

Pim Arlow
Founder
0417 286 314
pimarlow@bramblekitchenvq.com
Unit 6, 14 Talvery Crescelt
Wexholm TLB 5162

Have fun and thank you in advance for choosing to work on our job.

Reason: Thank you to everyone who has submitted their designs for an email footer. Looking at the designs most have been designed horizontally. Could I please also see some designs where all the elements are under each other in a stacked format. I have attached 2 images which I have grabbed from the internet to be used as an example.

```html
<!DOCTYPE html>
<html lang="en">
<head>
<meta charset="utf-8">
<title>Bramble Kitchen – Email Footer</title>
<link rel="stylesheet" href="https://fonts.googleapis.com/css2?family=Poppins:wght@400;600&display=swap">
<style>
  :root {
    --brand-orange: #ff8600;
    --ink: #231f20;
    --card: #ffffff;
    --backdrop: #e6e6e6;
  }
  * { box-sizing: border-box; margin: 0; padding: 0; }
  html, body {
    width: 1200px;
    height: 336px;
    overflow: hidden;
    background: var(--backdrop);
    font-family: "Poppins", sans-serif;
    color: var(--ink);
  }
  .footer-card {
    position: absolute;
    left: 38px;
    top: 29px;
    width: 1130px;
    height: 275px;
    background: var(--card);
    overflow: hidden;
  }
  .brand-name {
    position: absolute;
    left: 60px;
    top: 92px;
    width: 380px;
    color: var(--brand-orange);
    font-size: 34px;
    font-weight: 400;
    line-height: 1.2;
    text-align: center;
    white-space: nowrap;
  }
  .divider {
    position: absolute;
    left: 630px;
    top: 21px;
    width: 2px;
    height: 167px;
    background: var(--ink);
  }
  .contact {
    position: absolute;
    left: 659px;
    top: 16px;
    list-style: none;
  }
  .contact__person {
    font-size: 21px;
    line-height: 30px;
    margin-bottom: 10px;
  }
  .contact__name {
    color: var(--brand-orange);
    font-weight: 600;
  }
  .contact__role { font-weight: 400; }
  .contact__item {
    display: flex;
    align-items: flex-start;
    font-size: 20px;
    line-height: 28px;
    margin-bottom: 11px;
  }
  .contact__icon {
    flex: none;
    width: 17px;
    height: 17px;
    margin: 5px 10px 0 0;
    fill: var(--ink);
  }
  .wave {
    position: absolute;
    left: 0;
    bottom: 0;
    width: 1130px;
    height: 275px;
  }
  .wave__dark { fill: var(--ink); }
  .wave__band { fill: var(--brand-orange); }
</style>
</head>
<body>
  <div class="footer-card">
    <div class="brand-name">Bramble Kitchen</div>

    <div class="divider"></div>

    <ul class="contact">
      <li class="contact__person"><span class="contact__name">Pim Arlow</span> <span class="contact__role">, Founder</span></li>
      <li class="contact__item">
        <svg class="contact__icon" viewBox="0 0 16 16" aria-hidden="true">
          <path d="M3.2 1.5l2.3-.3 1.3 3.4-1.6 1.2c.7 1.7 2 3 3.7 3.8l1.2-1.6 3.4 1.3-.3 2.4c-.2.9-1 1.5-1.9 1.4C6.4 12.6 2.9 9 2 4c-.1-1.2.4-2.3 1.2-2.5z"/>
        </svg>
        <span>0417 286 314</span>
      </li>
      <li class="contact__item">
        <svg class="contact__icon" viewBox="0 0 16 16" aria-hidden="true">
          <path d="M1 6l7-4.5L15 6v8.5H1z M2.6 6.4L8 10l5.4-3.6L8 3z" fill-rule="evenodd"/>
        </svg>
        <span>pimarlow@bramblekitchenvq.com</span>
      </li>
      <li class="contact__item">
        <svg class="contact__icon" viewBox="0 0 16 16" aria-hidden="true">
          <path d="M8 0.5a5.3 5.3 0 0 0-5.3 5.3C2.7 9.8 8 15.5 8 15.5s5.3-5.7 5.3-9.7A5.3 5.3 0 0 0 8 .5zm0 7.3a2 2 0 1 1 0-4 2 2 0 0 1 0 4z"/>
        </svg>
        <span>Unit 6, 14 Talvery Crescelt<br>Wexholm TLB 5162</span>
      </li>
    </ul>

    <svg class="wave" viewBox="0 0 1130 275" preserveAspectRatio="none" aria-hidden="true">
      <path class="wave__dark" d="M0,232 C180,205 320,190 470,196 C640,204 700,250 860,238 C960,230 1050,205 1130,180 L1130,190 C1030,222 900,250 700,254 C470,258 250,232 0,239 Z"/>
      <path class="wave__band" d="M0,239 C250,232 470,258 700,254 C900,250 1030,222 1130,190 L1130,275 L0,275 Z"/>
    </svg>
  </div>
</body>
</html>
```